Farhan Jewellers Stationary Contest

Pakistan’s largest Jewellery, Diamond and luxury watches store requires professional stationery. We have a long list of are trusted clients since 1959, our third generation has successfully maintained and sustained the legacy and excellence in the sector.

We require stationery template as part of this contest. The stationery can be double sided.

We prefer a design that makes use of some of the premium business stationery printing options, such as foil stamping, embossing/debossing, painted edges, spot UV etc (doesn't have to use all these options, only what you feel works, but we are looking for a design that stands out and is memorable and these nice touches have that effect.)

We want an eye catching, innovative, high end professional looking stationery for an out of box design that blends well with our new logo (attached). We want the design to be an out of box solution, you may use any element to compliment the logo. You may consider incorporating watermark etc, highlighting our products (Gold and Diamond Jewellery in addition to Luxury watches)

Company details are as follows;

Company name: Farhan Jewellers
Contact Person: Tariq Naveed
Designation: Business Development Consultant
Mobile: +92 333 815 6042
Email: tariqnaveed@mailvora.com
Website: www.farhanjewellers-pk.net

Target Market(s)

Matrimonial, Elite & Businesses class, Upmarket

Font styles to use
Other font styles liked:
• Designers choice

Colors

Designer to choose colors to be used in the design.

Requirements
Must have
• Look and feel: Upmarket, innovative, Modern, Professional, graceful, Elegant, designer stuff.
Nice to have
• Unique design

```html
<!DOCTYPE html>
<html lang="en">
<head>
<meta charset="UTF-8">
<title>Farhan Jewellers – Business Card</title>
<link rel="stylesheet" href="https://fonts.googleapis.com/css2?family=Montserrat:wght@600;700&family=Open+Sans:wght@400&display=swap">
<style>
  :root {
    --backdrop: #3b3431;
    --card: #0d0d0d;
    --card-edge: #1a1a1a;
    --gold: #d4a43a;
    --ink-light: #f2f2f2;
  }
  * { margin: 0; padding: 0; box-sizing: border-box; }
  html, body {
    width: 1200px;
    height: 864px;
    overflow: hidden;
    background: var(--backdrop);
  }
  .canvas {
    position: relative;
    width: 1200px;
    height: 864px;
    display: flex;
    align-items: center;
    justify-content: center;
    gap: 50px;
  }
  .card {
    width: 540px;
    height: 310px;
    background: var(--card);
    border: 1px solid var(--card-edge);
    box-shadow: 0 18px 40px rgba(0,0,0,0.45);
    display: flex;
    flex-direction: column;
    align-items: center;
    justify-content: center;
    text-align: center;
  }
  .brand-mark {
    display: flex;
    flex-direction: column;
    align-items: center;
    gap: 10px;
  }
  .brand-dot {
    width: 30px;
    height: 30px;
    border-radius: 50%;
    background: var(--gold);
  }
  .brand-name {
    font-family: "Montserrat", sans-serif;
    font-weight: 700;
    color: var(--gold);
    text-transform: uppercase;
    letter-spacing: 2px;
  }
  .card--front .brand-name { font-size: 30px; }
  .card--back .brand-name { font-size: 22px; }
  .web {
    font-family: "Open Sans", sans-serif;
    color: var(--ink-light);
    letter-spacing: 2px;
  }
  .card--front .web { font-size: 15px; margin-top: 22px; }

  .contact { margin-top: 16px; }
  .person-name {
    font-family: "Montserrat", sans-serif;
    font-weight: 700;
    font-size: 17px;
    color: var(--gold);
    text-transform: uppercase;
    letter-spacing: 1px;
  }
  .person-title,
  .contact-line {
    font-family: "Open Sans", sans-serif;
    color: var(--ink-light);
    font-size: 14px;
    line-height: 1.5;
  }
  .card--back .web { font-size: 14px; line-height: 1.5; }
</style>
</head>
<body>
  <main class="canvas">
    <section class="card card--front" aria-label="Card front">
      <div class="brand-mark">
        <span class="brand-dot"></span>
        <span class="brand-name">Farhan Jewellers</span>
      </div>
      <p class="web">www.farhanjewellers-pk.net</p>
    </section>

    <section class="card card--back" aria-label="Card back">
      <div class="brand-mark">
        <span class="brand-dot"></span>
        <span class="brand-name">Farhan Jewellers</span>
      </div>
      <div class="contact">
        <p class="person-name">Tariq Naveed</p>
        <p class="person-title">Business Development Consultant</p>
        <p class="contact-line">P: +92 333 815 6042 &nbsp;E: tariqnaveed@mailvora.com</p>
        <p class="web">www.farhanjewellers-pk.net</p>
      </div>
    </section>
  </main>
</body>
</html>
```